Kettle Ledger Business Card design

We need a stand out business card design for Accounting practice based in Australia specialising in pubs, clubs and hotels. We help venues maximise margins, create time and manage cashflow. One club we have been working with for the last 6 months has increased revenue by 3% and margin by 5% in this time frame. We have a back office outsourced system that costs less than having a full time employee and also allows the venues the added benefit of:<br/>-using the office space to become a revenue generating opportunity. <br/>-a complete system to enhance governance, accountability and efficiency within their operation<br/>-52 weeks cover so no hassle to cover annual/sick .. leave<br/><br/>We would like to see designs that use the colours of our logo (green & blue).
Target Market(s)
Australian Pubs, Clubs & Hotels abookkeeping, accounting and tax services
Industry/Entity Type
Accountant
Contact Information for Business Card
Miriam Oakley CPA
Principal
Accountant Tax Agent
Miriam@KettleLedger-example.com.au
0418693142
www.kettleledger-example.com.au
Accounting / Payroll / Tax / SMSF / Technology
Colors
Designer to choose colors to be used in the design.
Look and feel
Each slider illustrates characteristics of the customer's brand and the style your logo design should communicate.

```html
<!DOCTYPE html>
<html lang="en">
<head>
<meta charset="utf-8">
<title>Kettle Ledger Business Card</title>
<link href="https://fonts.googleapis.com/css2?family=Roboto:wght@300;400;700;900&display=swap" rel="stylesheet">
<style>
  :root {
    --brand-blue: #1f3f8f;
    --brand-green: #17783a;
    --paper: #ebebeb;
    --ink-light: #ffffff;
    --backdrop: #d9d9d9;
  }
  * { box-sizing: border-box; margin: 0; padding: 0; }
  html, body {
    width: 1200px;
    height: 1021px;
    overflow: hidden;
    background: var(--backdrop);
    font-family: "Roboto", Arial, sans-serif;
  }
  .sheet {
    width: 1200px;
    height: 1021px;
    display: flex;
    flex-direction: column;
    align-items: center;
    justify-content: center;
    gap: 60px;
  }
  .card {
    position: relative;
    width: 620px;
    height: 360px;
    overflow: hidden;
    box-shadow: 0 6px 18px rgba(0,0,0,0.25);
  }

  /* Back of card */
  .card-back {
    background: var(--brand-blue);
    color: var(--ink-light);
  }
  .card-back .wordmark {
    position: absolute;
    top: 44px;
    left: 48px;
    display: flex;
    align-items: center;
    gap: 14px;
  }
  .wordmark-dot {
    width: 26px;
    height: 26px;
    border-radius: 50%;
    border: 3px solid currentColor;
  }
  .wordmark-name {
    font-weight: 900;
    font-size: 34px;
    letter-spacing: 0.5px;
  }
  .services {
    position: absolute;
    top: 124px;
    left: 0;
    right: 0;
    list-style: none;
    text-align: center;
    font-weight: 300;
    font-size: 19px;
    letter-spacing: 1.5px;
    line-height: 32px;
  }
  .credentials {
    position: absolute;
    right: 40px;
    left: 40px;
    bottom: 24px;
    display: flex;
    justify-content: space-between;
    align-items: flex-end;
  }
  .badge-round {
    width: 58px;
    height: 58px;
    border-radius: 50%;
    border: 2px solid rgba(255,255,255,0.8);
  }
  .badge-square {
    width: 64px;
    height: 52px;
    border: 2px solid var(--ink-light);
    background: rgba(255,255,255,0.9);
  }
  .badge-bar {
    width: 60px;
    height: 26px;
    border-top: 2px solid rgba(255,255,255,0.8);
    border-bottom: 2px solid rgba(255,255,255,0.8);
  }

  /* Front of card */
  .card-front {
    background: var(--paper);
  }
  .front-split {
    position: absolute;
    inset: 0;
  }
  .front-brand {
    position: absolute;
    top: 58px;
    left: 0;
    right: 0;
    display: flex;
    justify-content: center;
    align-items: center;
    gap: 16px;
    color: var(--brand-blue);
  }
  .front-brand .wordmark-name { font-size: 54px; }
  .front-brand .wordmark-dot { width: 34px; height: 34px; border-width: 4px; }
  .contact {
    position: absolute;
    top: 186px;
    left: 0;
    right: 0;
    text-align: center;
    color: var(--ink-light);
  }
  .contact-name { font-weight: 700; font-size: 20px; }
  .contact-role { font-weight: 300; font-size: 15px; line-height: 20px; }
  .contact-icons {
    display: flex;
    justify-content: center;
    gap: 10px;
    margin: 8px 0 4px;
  }
  .contact-icons svg { width: 14px; height: 14px; }
  .contact-lines { font-weight: 300; font-size: 15px; line-height: 20px; }
</style>
</head>
<body>
<main class="sheet">

  <section class="card card-back" aria-label="Business card back">
    <div class="wordmark">
      <span class="wordmark-dot"></span>
      <span class="wordmark-name">Kettle Ledger</span>
    </div>
    <ul class="services">
      <li>ACCOUNTING</li>
      <li>PAYROLL</li>
      <li>TAX</li>
      <li>SMSF</li>
      <li>TECHNOLOGY</li>
    </ul>
    <div class="credentials">
      <span class="badge-round" role="img" aria-label="Registration badge"></span>
      <span class="badge-square" role="img" aria-label="Professional membership badge"></span>
      <span class="badge-bar" role="img" aria-label="Institute membership badge"></span>
    </div>
  </section>

  <section class="card card-front" aria-label="Business card front">
    <svg class="front-split" viewBox="0 0 620 360" preserveAspectRatio="none" aria-hidden="true">
      <polygon points="0,150 620,160 620,360 0,360" fill="#1f3f8f"/>
    </svg>
    <div class="front-brand">
      <span class="wordmark-dot"></span>
      <span class="wordmark-name">Kettle Ledger</span>
    </div>
    <div class="contact">
      <p class="contact-name">Miriam Oakley CPA</p>
      <p class="contact-role">Principal</p>
      <p class="contact-role">Accountant Tax Agent</p>
      <div class="contact-icons">
        <svg viewBox="0 0 16 16" aria-label="Phone"><path d="M4 1l3 3-2 2c1 2 3 4 5 5l2-2 3 3-2 3C7 15 1 9 1 3z" fill="#fff"/></svg>
        <svg viewBox="0 0 16 16" aria-label="Email"><rect x="1.5" y="3.5" width="13" height="9" fill="none" stroke="#fff" stroke-width="1.4"/><path d="M1.5 3.5l6.5 5 6.5-5" fill="none" stroke="#fff" stroke-width="1.4"/></svg>
        <svg viewBox="0 0 16 16" aria-label="Website"><circle cx="8" cy="8" r="6.5" fill="none" stroke="#fff" stroke-width="1.3"/><ellipse cx="8" cy="8" rx="3" ry="6.5" fill="none" stroke="#fff" stroke-width="1.1"/><path d="M1.5 8h13" stroke="#fff" stroke-width="1.1"/></svg>
      </div>
      <div class="contact-lines">
        <p>0418693142</p>
        <p>Miriam@KettleLedger-example.com.au</p>
        <p>www.kettleledger-example.com.au</p>
      </div>
    </div>
  </section>

</main>
</body>
</html>
```